SkyvoraQ Business Cards and Stationary Design

Need a design for our business cards and stationary. I want to carry on the theme of the logo. I want the business cards to have a design on the back. I would like the business cards and the stationary to carry the same theme, design scheme, and branding

Target Market(s)

Airlines and Maintenance Facilities

Industry/Entity Type

Aviation

Contact Information for Business Card

Name
Position Title
Address: 4827 Tollbeck Lane, Fort Pierce, Florida, 34951
Office Number
Mobile Number
Email
Website

Font styles to use
Serif
Sans Serif

Colors

Designer to choose colors to be used in the design.

```html
<!DOCTYPE html>
<html lang="en">
<head>
<meta charset="utf-8">
<title>SkyvoraQ Business Card</title>
<link rel="stylesheet" href="https://fonts.googleapis.com/css2?family=Saira:wdth,wght@125,600&family=Arimo:wght@400;700&display=swap">
<style>
  :root {
    --backdrop: #cfcfcf;
    --backdrop-light: #e6e6e6;
    --card-black: #151515;
    --card-navy: #16264e;
    --brand-blue: #2e8fd2;
    --brand-blue-deep: #1f4f9a;
    --white: #ffffff;
  }
  * { margin: 0; padding: 0; box-sizing: border-box; }
  html, body { width: 1200px; height: 900px; overflow: hidden; }
  body {
    position: relative;
    background: radial-gradient(ellipse at center, var(--backdrop-light) 0%, var(--backdrop) 75%);
    font-family: "Arimo", Arial, sans-serif;
  }
  .card {
    position: absolute;
    top: 82px;
    width: 431px;
    height: 740px;
    overflow: hidden;
  }
  .card-front {
    left: 135px;
    background: var(--card-black);
    border-radius: 46px 0 46px 0;
  }
  .card-back {
    left: 642px;
    background: var(--card-navy);
    border-radius: 0 46px 0 46px;
    color: var(--white);
  }
  .front-emblem-area {
    position: absolute;
    left: 0;
    top: 42px;
    width: 431px;
    height: 494px;
    background: radial-gradient(ellipse 62% 58% at 52% 50%,
      rgba(46, 143, 210, 0.55) 0%,
      rgba(31, 79, 154, 0.45) 45%,
      rgba(21, 21, 21, 0) 100%);
  }
  .wordmark {
    position: absolute;
    left: 0; right: 0;
    text-align: center;
    font-family: "Saira", "Arial", sans-serif;
    font-weight: 600;
    font-stretch: 125%;
    white-space: nowrap;
  }
  .front-wordmark {
    top: 612px;
    font-size: 41px;
    line-height: 44px;
    letter-spacing: 6px;
    color: var(--brand-blue);
  }
  .front-url {
    top: 667px;
    font-size: 17px;
    line-height: 22px;
    letter-spacing: 5.5px;
    color: var(--brand-blue);
  }
  .back-wordmark {
    top: 240px;
    font-size: 33px;
    line-height: 38px;
    letter-spacing: 6px;
    color: var(--white);
  }
  .holder { position: absolute; left: 42px; top: 433px; }
  .holder-name { font-size: 21px; line-height: 26px; }
  .holder-title { font-size: 14px; margin-top: 2px; }
  .contact-list { position: absolute; left: 42px; top: 501px; list-style: none; }
  .contact-list li {
    display: flex; align-items: center;
    font-size: 16px; height: 26px;
  }
  .contact-list svg { width: 21px; height: 21px; margin-right: 8px; flex: none; }
  .address { position: absolute; left: 42px; top: 596px; font-size: 16px; line-height: 23px; font-style: normal; }
  .back-url {
    position: absolute; left: 0; right: 0; top: 692px;
    text-align: center; font-weight: 700; font-size: 15px; letter-spacing: 0.5px;
  }
</style>
</head>
<body>
  <section class="card card-front">
    <div class="front-emblem-area" role="img" aria-label="Large brand emblem decoration in blue on black"></div>
    <div class="wordmark front-wordmark">SKYVORAQ</div>
    <div class="wordmark front-url">WWW.SKYVORAQ.COM</div>
  </section>

  <section class="card card-back">
    <div class="wordmark back-wordmark">SKYVORAQ</div>

    <div class="holder">
      <div class="holder-name">Dorian M Whitcombe</div>
      <div class="holder-title">President &amp; CEO</div>
    </div>

    <ul class="contact-list">
      <li>
        <svg viewBox="0 0 20 20" aria-hidden="true"><circle cx="10" cy="10" r="10" fill="#fff"/><path d="M6.5 5.2l1.8-.4 1 2.4-1.1.9a6 6 0 0 0 2.8 2.8l.9-1.1 2.4 1-.4 1.8c-4 .4-7.8-3.4-7.4-7.4z" fill="#16264e"/></svg>
        (230) 555 0142
      </li>
      <li>
        <svg viewBox="0 0 20 20" aria-hidden="true"><circle cx="10" cy="10" r="10" fill="#fff"/><rect x="7" y="4.5" width="6" height="11" rx="1" fill="#16264e"/><rect x="8" y="6" width="4" height="5" fill="#fff"/></svg>
        (603) 555 0187
      </li>
      <li>
        <svg viewBox="0 0 20 20" aria-hidden="true"><circle cx="10" cy="10" r="10" fill="#fff"/><rect x="5" y="6.5" width="10" height="7" fill="#16264e"/><path d="M5.5 7l4.5 3.5L14.5 7" stroke="#fff" stroke-width="1" fill="none"/></svg>
        dorianwhitcombe@skyvoraq.net
      </li>
    </ul>

    <address class="address">4827 Tollbeck Lane<br>Fort Pierce, Florida, 34951</address>

    <div class="back-url">www.skyvoraq.com</div>
  </section>
</body>
</html>
```